Labels for fruit liqueur bottles

We are looking for a visual identity based on our logo, for fruit liqueur labels. To date, we have different liqueurs such as: lemon liqueur, orange liqueurs, mandarin liqueurs, grapefruit liqueurs. We will then create other liqueurs such as strawberry, apple or even apricot. Our goal is to have a single visual that we can adapt in different colors depending on the fruit used.

On the label there should be:
the logo
homemade
the name of the fruit (which can be changed depending on the product)
swiss-made
50cl
21°

Colors

Designer to choose colors to be used in the design.

Requirements
Must have
• a visual of liquor bottle labels, with the possibility of changing the background colors, depending on the fruit used
Nice to have
• something modern and nice to look at. We must be able to read the basic fruit in the blink of an eye. it is also possible to have a black or white or colored label background.

```html
<!DOCTYPE html>
<html lang="en">
<head>
<meta charset="utf-8">
<title>Homemade Lemon Liqueur – Label</title>
<link rel="stylesheet" href="https://fonts.googleapis.com/css2?family=Abril+Fatface&family=Oswald:wght@500;600&family=Poppins:wght@400;500&family=Roboto+Slab:wght@700&display=swap">
<style>
  :root {
    --page: #f3f3f1;
    --cream: #ebe9dd;
    --leaf-green: #7fa83a;
    --leaf-green-dark: #4d7a22;
    --art-light: #e6ecb8;
    --art-mid: #c9d97a;
    --brand-red: #d8452a;
    --ribbon-red: #b5262f;
    --ribbon-dark: #8c1a22;
    --white: #ffffff;
  }
  html, body {
    margin: 0;
    width: 900px;
    height: 1200px;
    overflow: hidden;
    background: var(--page);
  }
  .canvas {
    position: relative;
    width: 900px;
    height: 1200px;
  }
  .label {
    position: absolute;
    left: 70px;
    top: 160px;
    width: 760px;
    height: 880px;
    box-shadow: 0 6px 24px rgba(0,0,0,.12);
  }
  .brand-name {
    font-family: "Poppins", sans-serif;
    font-weight: 500;
    fill: var(--brand-red);
  }
  .brand-tagline {
    font-family: "Poppins", sans-serif;
    font-weight: 400;
    fill: var(--brand-red);
  }
  .kicker {
    font-family: "Oswald", sans-serif;
    font-weight: 600;
    fill: var(--white);
    stroke: var(--leaf-green-dark);
    stroke-width: 4;
    paint-order: stroke;
  }
  .fruit-name {
    font-family: "Abril Fatface", serif;
    fill: var(--white);
    stroke: var(--leaf-green-dark);
    stroke-width: 8;
    paint-order: stroke;
  }
  .product-type {
    font-family: "Oswald", sans-serif;
    font-weight: 600;
    fill: var(--white);
    stroke: var(--leaf-green-dark);
    stroke-width: 6;
    paint-order: stroke;
  }
  .ribbon-text {
    font-family: "Roboto Slab", serif;
    font-weight: 700;
    fill: var(--white);
  }
  .seal-text {
    font-family: "Poppins", sans-serif;
    font-weight: 500;
    fill: var(--white);
    letter-spacing: 1.5px;
  }
</style>
</head>
<body>
<main class="canvas">
  <svg class="label" viewBox="0 0 760 880" xmlns="http://www.w3.org/2000/svg">
    <defs>
      <linearGradient id="art-fill" x1="0" y1="0" x2="1" y2="1">
        <stop offset="0" stop-color="var(--art-light)"/>
        <stop offset="1" stop-color="var(--art-mid)"/>
      </linearGradient>
      <path id="seal-top" d="M338 715 A42 42 0 0 1 422 715"/>
      <path id="seal-bottom" d="M334 715 A46 46 0 0 0 426 715"/>
    </defs>

    <!-- label ground -->
    <rect class="label-cream" width="760" height="880" fill="var(--cream)"/>
    <polygon class="label-green" points="0,375 760,162 760,880 0,880" fill="var(--leaf-green)"/>

    <!-- fruit artwork area -->
    <rect class="fruit-art" x="8" y="22" width="380" height="270" rx="40"
          fill="url(#art-fill)" opacity="0.85"
          role="img" aria-label="Engraved illustration of two lemons on a leafy branch with blossoms"/>

    <!-- brand -->
    <g class="brand">
      <circle cx="534" cy="120" r="40" fill="var(--brand-red)"/>
      <text class="brand-name" x="514" y="207" font-size="34" text-anchor="middle" textLength="265" lengthAdjust="spacingAndGlyphs">CASA VERANI</text>
      <text class="brand-tagline" x="514" y="230" font-size="17" text-anchor="middle">liqueur de fruits</text>
    </g>

    <!-- product title -->
    <text class="kicker" x="115" y="372" font-size="48" textLength="208" lengthAdjust="spacingAndGlyphs"
          transform="rotate(-6 220 350)">HOMEMADE</text>
    <text class="fruit-name" x="112" y="518" font-size="180" textLength="535" lengthAdjust="spacingAndGlyphs">LEMON</text>
    <text class="product-type" x="326" y="616" font-size="112" textLength="320" lengthAdjust="spacingAndGlyphs">LIQUEUR</text>

    <!-- ribbon -->
    <g class="ribbon">
      <path d="M122 690 L160 680 L600 680 L638 690 L638 740 L600 750 L160 750 L122 740 Z" fill="var(--ribbon-red)" stroke="var(--ribbon-dark)" stroke-width="3"/>
      <circle cx="136" cy="715" r="9" fill="var(--ribbon-dark)"/>
      <circle cx="624" cy="715" r="9" fill="var(--ribbon-dark)"/>
      <text class="ribbon-text" x="240" y="727" font-size="32" text-anchor="middle">50CL</text>
      <text class="ribbon-text" x="524" y="727" font-size="32" text-anchor="middle">21°</text>
      <circle class="origin-seal" cx="380" cy="715" r="62" fill="var(--ribbon-red)" stroke="var(--ribbon-dark)" stroke-width="4"/>
      <path d="M372 692 h16 v15 h15 v16 h-15 v15 h-16 v-15 h-15 v-16 h15 Z" fill="var(--white)"/>
      <text class="seal-text" font-size="12"><textPath href="#seal-top" startOffset="50%" text-anchor="middle">SWISS MADE</textPath></text>
      <text class="seal-text" font-size="12" dy="9"><textPath href="#seal-bottom" startOffset="50%" text-anchor="middle">100% QUALITY</textPath></text>
    </g>
  </svg>
</main>
</body>
</html>
```